OrbitHaven Product

There are two interfaces: Admin Interface and Employee Interface.

Admin Interface: the admin interface is for the administrator inside the company. He will be able to

enter emails of employees and send them an email invitation with a link that takes the employees to fill

a profile and choose their topic of interests.

Employee Interface: the employee interface is for the employee inside the company.

1. Employee receives email invitation with a link.

2. Employee clicks on the link.

3. Employee fills his profile and chooses the health topic of interest.

4. Employee starts to watch the videos he selected.

Currently we have screenshots based on .net generic designs. We need the designs to be sliced and html

formatted.

Target Market(s)

Arab Countries

Industry/Entity Type

Health And Wellness

Coding

Coded - Design and coding required

Number of Pages Required

5+ page

Colors
b768aa

Requirements
Must have
• * admin interface:
• it has side sections, for example: staff contact list, broadcast notifications, invitation template, personalized content, settings, analytics and log out.
• * 3 pages for employee profile creation:
• - page# 1: first name, last name, date of birth, gender, marital status, mobile number, country and email
• - page#2: username, password and confirm your password
• - page#3: choose content: this is a checklist that user choose from; it has the category name above.

```html
<!DOCTYPE html>
<html lang="en">
<head>
<meta charset="utf-8">
<title>Vitalyn – Welcome</title>
<link href="https://fonts.googleapis.com/css2?family=Arimo:wght@400;700&display=swap" rel="stylesheet">
<style>
:root{
  --brand:#b768aa;
  --brand-dark:#9a4f8e;
  --navy:#212a3e;
  --navy-line:#2b3450;
  --footer:#232b40;
  --nav-text:#8990a6;
  --page:#f7f8fa;
  --text:#6e7690;
  --field:#f7f8fa;
  --field-border:#dde1e8;
  --panel-border:#e3e6ec;
  --muted-btn:#7d859f;
  --notice:#e6edfb;
  --white:#ffffff;
}
*{box-sizing:border-box;margin:0;padding:0}
html,body{width:1200px;height:924px;overflow:hidden}
body{font-family:"Arimo",Arial,sans-serif;background:var(--page);position:relative;color:var(--text)}
.topbar{position:absolute;left:0;top:0;width:1200px;height:97px;background:var(--white);border-bottom:2px solid #eceef2}
.brand{position:absolute;left:28px;top:30px;display:flex;align-items:center;gap:12px}
.brand-dot{width:36px;height:36px;border-radius:50%;background:var(--brand)}
.brand-name{font-size:26px;font-weight:700;color:#1f4e6b;letter-spacing:1px}
.top-icon{position:absolute;top:34px;width:28px;height:28px}
.badge{position:absolute;top:-5px;right:-5px;width:16px;height:16px;border-radius:50%;background:var(--brand);color:#fff;font-size:10px;line-height:16px;text-align:center}
.skip{position:absolute;left:1061px;top:31px;width:89px;height:35px;border:1px solid #dcdfe5;border-radius:3px;color:#7b8196;font-size:15px;line-height:33px;text-align:center}
.sidebar{position:absolute;left:0;top:97px;width:264px;height:743px;background:var(--navy)}
.nav-item{height:57px;border-bottom:2px solid var(--navy-line);display:flex;align-items:center;padding-left:32px;gap:22px;color:var(--nav-text);font-size:14px;font-weight:700;text-transform:uppercase}
.nav-item svg{width:19px;height:19px;fill:var(--nav-text);flex:none}
.nav-item.active{background:var(--brand);color:#fff;border-bottom-color:var(--brand)}
.nav-item.active svg{fill:#fff}
.main{position:absolute;left:264px;top:97px;width:936px;height:743px}
.title{position:absolute;top:34px;width:936px;text-align:center;font-size:25px;font-weight:700;color:#6a728a}
.stepper{position:absolute;left:218px;top:104px;width:510px;height:46px}
.track{position:absolute;left:22px;right:22px;top:18px;height:10px;background:linear-gradient(#d3d3d3,#bdbdbd);border-top:1px solid #e6e6e6}
.step{position:absolute;top:0;width:46px;height:46px;border-radius:50%;background:#d9d9d9;border:3px solid #ececec;box-shadow:0 0 0 1px #c8c8c8}
.step span{display:block;width:34px;height:34px;margin:3px;border-radius:50%;background:#b4b4b4;color:#fff;font-size:22px;font-weight:700;line-height:34px;text-align:center}
.step.current span{background:linear-gradient(var(--brand),var(--brand-dark))}
.step-label{position:absolute;top:166px;width:200px;text-align:center;font-size:15px;color:#737b92}
.panel{position:absolute;left:31px;top:219px;width:875px;height:391px;background:var(--white);border:1px solid var(--panel-border)}
.field{position:absolute;width:400px}
.field label{display:block;font-size:15px;color:#737b92;margin-left:2px;height:20px}
.field label b{color:var(--brand);font-weight:400}
.field .input{margin-top:10px;height:46px;background:var(--field);border:1px solid var(--field-border);border-radius:4px}
.toggle{position:absolute;left:21px;top:222px;display:flex;align-items:center;gap:9px;font-size:14px;color:#737b92}
.toggle i{width:20px;height:20px;border-radius:50%;border:1px solid #cfd3da;background:linear-gradient(#fff 50%,#e8e9ec 50%)}
.notice{position:absolute;left:21px;top:283px;width:834px;height:59px;background:var(--notice);border-radius:4px;font-size:14px;color:#737b92;padding:20px 0 0 18px}
.notice .close{position:absolute;right:20px;top:22px;width:12px;height:12px}
.actions{position:absolute;right:30px;top:632px;display:flex;gap:4px}
.btn{height:39px;border-radius:3px;color:#fff;font-size:15px;line-height:39px;text-align:center;background:var(--muted-btn)}
.btn.primary{background:var(--brand)}
.footer{position:absolute;left:0;top:840px;width:1200px;height:84px;background:var(--footer);color:#fff;font-size:15px}
.footer p{position:absolute;left:264px;width:852px;top:36px;text-align:center}
</style>
</head>
<body>
<header class="topbar">
  <div class="brand"><span class="brand-dot"></span><span class="brand-name">VITALYN</span></div>
  <div class="top-icon" style="left:962px">
    <svg viewBox="0 0 28 28" width="28" height="28" fill="none" stroke="#6a6f7d" stroke-width="1.8"><path d="M7 20V12a7 7 0 0 1 14 0v8l2 2H5z"/><path d="M11 24a3 3 0 0 0 6 0"/></svg>
    <span class="badge">2</span>
  </div>
  <div class="top-icon" style="left:1016px">
    <svg viewBox="0 0 28 28" width="28" height="28" fill="none" stroke="#6a6f7d" stroke-width="1.8"><rect x="3" y="7" width="22" height="16" rx="2"/><path d="M3 9l11 8 11-8"/></svg>
    <span class="badge">5</span>
  </div>
  <div class="skip">SKIP</div>
</header>

<nav class="sidebar">
  <div class="nav-item active"><svg viewBox="0 0 20 20"><path d="M10 3a8 8 0 0 0-8 8c0 2 .7 3.8 2 5h12a8 8 0 0 0-6-13zm1 9a1.5 1.5 0 1 1-2-1l3-4z"/></svg>Dashboard</div>
  <div class="nav-item"><svg viewBox="0 0 20 20"><circle cx="10" cy="6" r="3"/><circle cx="4" cy="8" r="2.3"/><circle cx="16" cy="8" r="2.3"/><path d="M5 17a5 5 0 0 1 10 0zM0 16a4 4 0 0 1 5-3.5 6 6 0 0 0-1 3.5zM20 16a4 4 0 0 0-5-3.5 6 6 0 0 1 1 3.5z"/></svg>Emplotees</div>
  <div class="nav-item"><svg viewBox="0 0 20 20"><path d="M2 4h16v12H2zm2 2v.5l6 4.5 6-4.5V6zm0 3v5h12V9l-6 4.5z"/></svg>Send Invitation</div>
  <div class="nav-item"><svg viewBox="0 0 20 20"><path d="M4 2h8l4 4v12H4zm2 2v12h8V7h-3V4zm1 6h4v4H7zm4 1 2-1v4l-2-1z"/></svg>Videos</div>
  <div class="nav-item"><svg viewBox="0 0 20 20"><path d="M3 3h14v14H3zm2 2v10h10V5z"/></svg>Banner</div>
  <div class="nav-item"><svg viewBox="0 0 20 20"><ellipse cx="8" cy="8" rx="7" ry="5.5"/><ellipse cx="14" cy="13" rx="6" ry="4.5"/></svg>SMS Template</div>
  <div class="nav-item"><svg viewBox="0 0 20 20"><path d="M10 2a8 8 0 1 0 4 15l-.8-1.5A6.3 6.3 0 1 1 16.3 10v1a1.3 1.3 0 0 1-2.6 0V6h-1.6v.8A4 4 0 1 0 13 13a3 3 0 0 0 5-2v-1a8 8 0 0 0-8-8zm0 10.3a2.3 2.3 0 1 1 0-4.6 2.3 2.3 0 0 1 0 4.6z"/></svg>Email Template</div>
  <div class="nav-item"><svg viewBox="0 0 20 20"><path d="M7 3h2l.4 2 1.6.9 1.8-1 1.4 1.4-1 1.8.7 1.6 2 .4v2l-2 .4-.7 1.6 1 1.8-1.4 1.4-1.8-1-1.6.7L9 18H7l-.4-2-1.6-.7-1.8 1-1.4-1.4 1-1.8L2 11.5l-2-.4v-2l2-.4.7-1.6-1-1.8L3 3.9l1.8 1L6.6 5zm1 5a2.5 2.5 0 1 0 0 5 2.5 2.5 0 0 0 0-5z"/></svg>Settings</div>
  <div class="nav-item"><svg viewBox="0 0 20 20"><path d="M9 1h2v9H9zM5.5 4.2l1.3 1.5a6 6 0 1 0 6.4 0l1.3-1.5a8 8 0 1 1-9 0z"/></svg>Log Out</div>
</nav>

<main class="main">
  <h1 class="title">WELCOME</h1>
  <div class="stepper">
    <div class="track"></div>
    <div class="step current" style="left:0"><span>1</span></div>
    <div class="step" style="left:232px"><span>2</span></div>
    <div class="step" style="left:464px"><span>3</span></div>
  </div>
  <div class="step-label" style="left:141px">Email Settings</div>
  <div class="step-label" style="left:370px">Upload Contacts</div>
  <div class="step-label" style="left:600px">Send Invitation</div>

  <section class="panel">
    <div class="field" style="left:20px;top:35px"><label>Email <b>*</b></label><div class="input"></div></div>
    <div class="field" style="left:454px;top:35px"><label>Password <b>*</b></label><div class="input"></div></div>
    <div class="field" style="left:20px;top:125px"><label>SMTP <b>*</b></label><div class="input"></div></div>
    <div class="field" style="left:454px;top:125px"><label>Port No<b>*</b></label><div class="input"></div></div>
    <div class="toggle"><i></i>Smtp Secure</div>
    <div class="notice">Emails will be sent using Vitalyn gateway in case you didn't fill the above information!
      <svg class="close" viewBox="0 0 12 12"><path d="M2 2l8 8M10 2l-8 8" stroke="#7d859f" stroke-width="2.6"/></svg>
    </div>
  </section>

  <div class="actions">
    <div class="btn primary" style="width:118px">PREVIOUS</div>
    <div class="btn" style="width:87px">NEXT</div>
    <div class="btn" style="width:87px">FINISH</div>
    <div class="btn" style="width:87px">CANCEL</div>
  </div>
</main>

<footer class="footer"><p>Copyright © 2016 Vitalyn. All rights reserved</p></footer>
</body>
</html>
```